Threshold: A Biblical Short Story Collection

I'm looking for a book cover for a biblical short story retelling: black background, with the image of a wine goblet (ancient looking if at all possible) filled with water, with a trace of red wine indicating that it is changing. The title is Threshold and the subtitle is A Biblical Short Story Collection. The author name is Nora Quince.

```html
<!DOCTYPE html>
<html lang="en">
<head>
<meta charset="utf-8">
<title>Threshold: A Biblical Short Story Collection</title>
<link rel="stylesheet" href="https://fonts.googleapis.com/css2?family=Cinzel:wght@400&family=Josefin+Sans:wght@400&family=Open+Sans:wght@400&display=swap">
<style>
  :root {
    --ink-black: #000000;
    --title-red: #b0132f;
    --text-white: #ffffff;
    --goblet-mid: #4a4442;
    --goblet-dark: #2b2725;
    --wine-red: #8c0f1c;
  }
  html, body {
    margin: 0;
    padding: 0;
    width: 800px;
    height: 1200px;
    overflow: hidden;
    background: var(--ink-black);
  }
  .cover {
    position: relative;
    width: 800px;
    height: 1200px;
    background: var(--ink-black);
    overflow: hidden;
  }
  .cover__title {
    position: absolute;
    top: 143px;
    left: 0;
    width: 800px;
    margin: 0;
    text-align: center;
    font-family: "Cinzel", serif;
    font-weight: 400;
    font-size: 96px;
    line-height: 1;
    color: var(--title-red);
  }
  .cover__subtitle {
    position: absolute;
    top: 297px;
    left: 0;
    width: 800px;
    margin: 0;
    text-align: center;
    font-family: "Open Sans", sans-serif;
    font-weight: 400;
    font-size: 32px;
    line-height: 1;
    letter-spacing: 0.5px;
    color: var(--text-white);
  }
  .cover__art {
    position: absolute;
    top: 400px;
    left: 230px;
    width: 430px;
    height: 610px;
  }
  .cover__author {
    position: absolute;
    top: 1081px;
    left: 0;
    width: 800px;
    margin: 0;
    padding-left: 14px;
    box-sizing: border-box;
    text-align: center;
    font-family: "Josefin Sans", sans-serif;
    font-weight: 400;
    font-size: 46px;
    line-height: 1;
    letter-spacing: 14px;
    color: var(--text-white);
  }
</style>
</head>
<body>
  <main class="cover">
    <h1 class="cover__title">THRESHOLD</h1>
    <p class="cover__subtitle">A BIBLICAL SHORT STORY COLLECTION</p>
    <svg class="cover__art" viewBox="0 0 430 610" role="img" aria-label="Photograph of an ancient carved wooden goblet, water splashing from its rim while a trace of red wine spills down its side and pools at the base">
      <defs>
        <radialGradient id="goblet-glow" cx="0.45" cy="0.42" r="0.55">
          <stop offset="0" stop-color="var(--goblet-mid)"/>
          <stop offset="0.45" stop-color="var(--goblet-dark)"/>
          <stop offset="0.78" stop-color="#3a0a10"/>
          <stop offset="1" stop-color="var(--ink-black)" stop-opacity="0"/>
        </radialGradient>
      </defs>
      <rect class="cover__art-area" x="0" y="0" width="430" height="610" fill="url(#goblet-glow)"/>
    </svg>
    <p class="cover__author">NORA QUINCE</p>
  </main>
</body>
</html>
```